vantoreq realty business card

We need a Business card for our new business. The logo was designed by BrushQuill, and the text We want on the back is:
REAL ESTATE INVESTMENTS
- BUY, RENOVATE, SELL AND RENT RESIDENTIAL PROPERTIES
- FULL HOME REHABBING , REMODELING AND INTERIOR DESIGN
- HOME STAGING SERVICES
- WHOLESALE INVESTOR PROPERTIES
- MAKE CASH OFFERS ON HOUSES IN ANY CONDITION AND IN ANY SITUATION
- PRIVATE MONEY INVESTOR PROGRAMS WITH 6-12% RETURNS
- PAY CASH REWARDS FOR REFFERALS
- CONCIERGE SERVICE

Business

```html
<!DOCTYPE html>
<html lang="en">
<head>
<meta charset="utf-8">
<title>vantoreq Realty – Business Card</title>
<link rel="stylesheet" href="https://fonts.googleapis.com/css2?family=Barlow:wght@300;400&family=Barlow+Semi+Condensed:wght@500;600&display=swap">
<style>
  :root {
    --backdrop: #f2f2f2;
    --card: #ffffff;
    --teal: #5bbccf;
    --ink-grey: #7c7f84;
    --tag-grey: #8a8d91;
    --card-shadow: 0 10px 28px rgba(0, 0, 0, 0.08), 0 2px 6px rgba(0, 0, 0, 0.05);
  }
  * { box-sizing: border-box; margin: 0; padding: 0; }
  html, body {
    width: 1200px;
    height: 1000px;
    overflow: hidden;
    background: var(--backdrop);
  }
  .canvas {
    position: relative;
    width: 1200px;
    height: 1000px;
  }
  .card {
    position: absolute;
    width: 600px;
    height: 343px;
    background: var(--card);
    box-shadow: var(--card-shadow);
    overflow: hidden;
  }

  /* Back of card: services list */
  .card-back { left: 70px; top: 140px; }
  .services-band {
    height: 62px;
    background: var(--teal);
    display: flex;
    align-items: center;
    padding-left: 34px;
  }
  .services-title {
    font-family: "Barlow Semi Condensed", sans-serif;
    font-weight: 600;
    font-size: 34px;
    letter-spacing: 0.5px;
    color: #ffffff;
  }
  .services-list {
    list-style: none;
    padding: 26px 34px 0;
  }
  .services-list li {
    font-family: "Barlow Semi Condensed", sans-serif;
    font-weight: 500;
    font-size: 15.5px;
    line-height: 27px;
    color: var(--ink-grey);
    letter-spacing: 0.2px;
  }
  .services-list li::before {
    content: "- ";
    color: var(--teal);
  }

  /* Front of card: brand */
  .card-front {
    left: 530px;
    top: 530px;
    display: flex;
    flex-direction: column;
    align-items: center;
    justify-content: center;
  }
  .brand-mark {
    width: 22px;
    height: 22px;
    background: var(--teal);
    margin-bottom: 18px;
  }
  .brand-name {
    font-family: "Barlow", sans-serif;
    font-weight: 300;
    font-size: 34px;
    color: var(--teal);
    letter-spacing: 0.5px;
  }
  .brand-tagline {
    font-family: "Barlow", sans-serif;
    font-weight: 400;
    font-size: 15px;
    letter-spacing: 2.6px;
    color: var(--tag-grey);
    margin-top: 6px;
  }
</style>
</head>
<body>
<main class="canvas">
  <section class="card card-back" aria-label="Card back">
    <div class="services-band">
      <h2 class="services-title">REAL ESTATE INVESTMENTS</h2>
    </div>
    <ul class="services-list">
      <li>BUY, RENOVATE, SELL AND RENT RESIDENTIAL PROPERTIES</li>
      <li>FULL HOME REHABBING , REMODELING AND INTERIOR DESIGN</li>
      <li>HOME STAGING SERVICES</li>
      <li>WHOLESALE INVESTOR PROPERTIES</li>
      <li>MAKE CASH OFFERS ON HOUSES IN ANY CONDITION AND IN ANY SITUATION</li>
      <li>PRIVATE MONEY INVESTOR PROGRAMS WITH 6-12% RETURNS</li>
      <li>PAY CASH REWARDS FOR REFFERALS</li>
      <li>CONCIERGE SERVICE</li>
    </ul>
  </section>

  <section class="card card-front" aria-label="Card front">
    <span class="brand-mark" aria-hidden="true"></span>
    <h1 class="brand-name">VANTOREQ Realty</h1>
    <p class="brand-tagline">REAL ESTATE SOLUTIONS</p>
  </section>
</main>
</body>
</html>
```